Lumora Business Card Design

hello,
we are looking for a business card design for our Fintech Company. We are credit card processing company that is also expanding in to the crypto market. We will be focusing on crypto processing, with a crypto wallet and crypto exchange. We like the purple in the logo. We want something modern and sophisticated but at the same time simple and trust worthy to work with banks.

Industry/Entity Type

Fintech

Logo Text

Lumora

```html
<!DOCTYPE html>
<html lang="en">
<head>
<meta charset="utf-8">
<title>Lumora Business Card</title>
<link rel="stylesheet" href="https://fonts.googleapis.com/css2?family=Montserrat:wght@700&family=Roboto:wght@400;500&display=swap">
<style>
  :root {
    --navy: #1b2d55;
    --purple: #4b3aa8;
    --paper: #f2f2f2;
    --ink: #333940;
    --backdrop: #e4e3e0;
  }
  * { box-sizing: border-box; margin: 0; padding: 0; }
  html, body { width: 1200px; height: 960px; overflow: hidden; }
  body {
    background: var(--backdrop);
    font-family: "Roboto", Arial, sans-serif;
    display: flex;
    flex-direction: column;
    align-items: center;
    justify-content: center;
    gap: 40px;
  }
  .card {
    position: relative;
    width: 760px;
    height: 434px;
    box-shadow: 0 6px 18px rgba(0,0,0,0.12);
  }
  .card--front {
    background: var(--navy);
    display: flex;
    align-items: center;
    justify-content: center;
  }
  .card--back { background: var(--paper); }

  .brand { display: flex; align-items: center; gap: 16px; }
  .brand__dot { border-radius: 50%; flex: none; }
  .brand__name { font-family: "Roboto", Arial, sans-serif; font-weight: 500; letter-spacing: 1px; }

  .card--front .brand__dot { width: 58px; height: 58px; background: #ffffff; }
  .card--front .brand__name { font-size: 82px; color: #ffffff; }

  .card--back .brand { position: absolute; top: 70px; right: 64px; gap: 12px; }
  .card--back .brand__dot { width: 40px; height: 40px; background: var(--navy); }
  .card--back .brand__name { font-size: 56px; color: var(--navy); }

  .divider {
    position: absolute;
    left: 262px;
    right: 64px;
    top: 206px;
    height: 2px;
    background: var(--purple);
  }
  .accent-bar {
    position: absolute;
    left: 48px;
    top: 244px;
    width: 22px;
    height: 36px;
    background: var(--navy);
  }
  .person { position: absolute; left: 94px; top: 186px; }
  .person__name {
    font-family: "Montserrat", Arial, sans-serif;
    font-weight: 700;
    font-size: 19px;
    letter-spacing: 1px;
    color: var(--navy);
    text-transform: uppercase;
  }
  .person__role { font-size: 17px; color: var(--purple); margin-top: 2px; }

  .contacts { position: absolute; left: 94px; top: 262px; list-style: none; }
  .contacts li {
    display: flex; align-items: center; gap: 8px;
    font-size: 18px; color: var(--ink); line-height: 26px;
  }
  .contacts svg { width: 16px; height: 16px; flex: none; }

  .address {
    position: absolute;
    right: 64px;
    top: 228px;
    text-align: right;
    font-size: 18px;
    line-height: 24px;
    color: var(--ink);
    font-style: normal;
  }
</style>
</head>
<body>
  <section class="card card--front" aria-label="Card front">
    <div class="brand">
      <span class="brand__dot"></span>
      <span class="brand__name">Lumora</span>
    </div>
  </section>

  <section class="card card--back" aria-label="Card back">
    <div class="brand">
      <span class="brand__dot"></span>
      <span class="brand__name">Lumora</span>
    </div>

    <div class="divider"></div>
    <div class="accent-bar"></div>

    <div class="person">
      <p class="person__name">Marcus Hale</p>
      <p class="person__role">Founder &amp; CEO</p>
    </div>

    <ul class="contacts">
      <li>
        <svg viewBox="0 0 16 16" aria-hidden="true"><path fill="#1b2d55" d="M3 1h3l1.5 3.5-2 1.3a9 9 0 0 0 4.7 4.7l1.3-2L15 10v3a2 2 0 0 1-2 2A12 12 0 0 1 1 3a2 2 0 0 1 2-2z"/></svg>
        555-014-2738
      </li>
      <li>
        <svg viewBox="0 0 16 16" aria-hidden="true"><rect x="1" y="3" width="14" height="10" fill="#1b2d55"/><path d="M1.5 3.5 8 9l6.5-5.5" fill="none" stroke="#f2f2f2" stroke-width="1.3"/></svg>
        info@lumora.com
      </li>
      <li>
        <svg viewBox="0 0 16 16" aria-hidden="true"><g fill="none" stroke="#1b2d55" stroke-width="1.3"><circle cx="8" cy="8" r="6.5"/><ellipse cx="8" cy="8" rx="3" ry="6.5"/><path d="M1.5 8h13M2.5 4.8h11M2.5 11.2h11"/></g></svg>
        www.lumora.com
      </li>
    </ul>

    <address class="address">
      1820 Harbor View Drive<br>
      Suite 210 Bayside Road<br>
      California 90412
    </address>
  </section>
</body>
</html>
```